Memento Mori Calendar

I’m looking for a graphic designer to create a Memento Mori–style life calendar that captures the essence of QUILNEXA — minimal, timeless, and deeply philosophical.

The design should be black and white only, with a refined, clean aesthetic and a sense of stillness and precision.
It should feel modern yet eternal, reflecting the themes of time, mortality, and presence.

Deliverables (Print-Ready Files):

24 x 30 in

24 x 32 in

24 x 36 in

A1 (594 x 841 mm)

All formats should be high-resolution and ready for professional printing (300 DPI, CMYK).

Design Requirements:

The calendar layout should follow the Memento Mori life calendar concept (weeks of life represented as small squares or circles).

The overall tone: minimal, meditative, monochrome.

Include the brand name: QUILNEXA (in an elegant, understated placement).

Add the following quote at the bottom or in a subtle position:

“Life can only be understood backwards; but it must be lived forwards.”
— Anselm Brodtvik

Target Market(s)

The QUILNEXA audience consists of urban, creative individuals aged 25 to 45, belonging to a middle to upper-middle income class. They lead conscious, quietly ambitious lives, seeking balance between inner depth and modern design. Their values center on awareness, presence, authenticity, and emotional depth, reflected in their preference for a monochrome, minimal, and timeless aesthetic. They tend to be introverted, reflective, and spiritually curious, drawn to brands that embody meaning and restraint rather than excess. Their cultural and stylistic affinities include Vinth, Polde, Ro Sefi, The Garden of Hours, Dussant, and Varolé — labels that share QUILNEXAs devotion to simplicity, substance, and subtle ritual.

Font styles to use
Serif
Sans Serif

Colors

Designer to choose only greyscale colors for use in the design.

Requirements
Must have
• The calendar layout should follow the Memento Mori life calendar concept (weeks of life represented as small squares or circles). The overall tone: minimal, meditative, monochrome. Include the brand name: trvolquen (in an elegant, understated placement). Add the following quote at the bottom or in a subtle position: “Life can only be understood backwards; but it must be lived forwards.” — Anselm Brodtvik

```html
<!DOCTYPE html>
<html lang="en">
<head>
<meta charset="utf-8">
<title>Memento Mori — QUILNEXA Life Calendar</title>
<link rel="stylesheet" href="https://fonts.googleapis.com/css2?family=Inter:wght@400;500;600;700&display=swap">
<style>
  :root {
    --paper: #ffffff;
    --ink: #000000;
    --grid-ink: #3a3a3a;
    --rule: #1a1a1a;
  }
  html, body {
    margin: 0;
    padding: 0;
    width: 940px;
    height: 1200px;
    overflow: hidden;
    background: var(--paper);
  }
  .poster {
    display: block;
    width: 940px;
    height: 1200px;
    font-family: "Inter", sans-serif;
  }
  .title { font-size: 93px; font-weight: 500; letter-spacing: -2px; fill: var(--ink); }
  .axis-label { font-size: 13px; font-weight: 700; fill: var(--ink); letter-spacing: 0.3px; }
  .week-number, .year-number { font-size: 8.5px; font-weight: 500; fill: var(--ink); }
  .brand-badge { fill: var(--ink); }
  .brand-name { font-size: 20px; font-weight: 600; fill: var(--paper); letter-spacing: 0.5px; }
  .quote, .quote-author { font-size: 14.5px; font-weight: 400; fill: var(--ink); }
  .rule { stroke: var(--rule); stroke-width: 0.8; }
  .marker { fill: var(--ink); }
</style>
</head>
<body>
<svg class="poster" viewBox="0 0 940 1200" xmlns="http://www.w3.org/2000/svg" role="img" aria-label="Memento Mori life calendar: 80 years of 52 weeks">
  <defs>
    <pattern id="week-cell" width="13.9" height="10.56" patternUnits="userSpaceOnUse">
      <rect x="0.4" y="0.4" width="6.6" height="6.6" fill="none" stroke="var(--grid-ink)" stroke-width="0.8"/>
    </pattern>
    <rect id="half-decade" width="361.4" height="105.6" fill="url(#week-cell)"/>
    <g id="week-markers" class="marker">
      <circle cx="183.1" cy="0" r="1.6"/>
      <circle cx="252.6" cy="0" r="1.6"/>
      <circle cx="322.1" cy="0" r="1.6"/>
      <circle cx="391.6" cy="0" r="1.6"/>
      <circle cx="461.1" cy="0" r="1.6"/>
      <circle cx="547.2" cy="0" r="1.6"/>
      <circle cx="616.7" cy="0" r="1.6"/>
      <circle cx="686.2" cy="0" r="1.6"/>
      <circle cx="755.7" cy="0" r="1.6"/>
      <circle cx="825.2" cy="0" r="1.6"/>
    </g>
    <g id="year-markers" class="marker">
      <circle cx="112" cy="0" r="2.2"/>
      <circle cx="874" cy="0" r="2.2"/>
    </g>
  </defs>

  <!-- Brand -->
  <rect class="brand-badge" x="712" y="52" width="154" height="34" rx="7"/>
  <text class="brand-name" x="789" y="76" text-anchor="middle">QUILNEXA</text>

  <!-- Title -->
  <text class="title" transform="translate(99,1091) rotate(-90)">Memento Mori</text>

  <!-- Week axis -->
  <text class="axis-label" x="124" y="117">WEEK</text>
  <rect class="marker" x="199" y="115" width="11" height="3"/>
  <line class="rule" x1="210" y1="117.5" x2="862" y2="117.5"/>
  <g class="week-numbers" text-anchor="middle">
    <text class="week-number" x="183.1" y="134">5</text>
    <text class="week-number" x="252.6" y="134">10</text>
    <text class="week-number" x="322.1" y="134">15</text>
    <text class="week-number" x="391.6" y="134">20</text>
    <text class="week-number" x="461.1" y="134">25</text>
    <text class="week-number" x="547.2" y="134">30</text>
    <text class="week-number" x="616.7" y="134">35</text>
    <text class="week-number" x="686.2" y="134">40</text>
    <text class="week-number" x="755.7" y="134">45</text>
    <text class="week-number" x="825.2" y="134">50</text>
  </g>

  <!-- Year axis -->
  <text class="axis-label" transform="translate(892,144) rotate(90)">YEAR</text>
  <rect class="marker" x="890" y="192" width="8" height="2.6"/>
  <line class="rule" x1="891" y1="194" x2="891" y2="1088"/>
  <g class="year-numbers" text-anchor="end">
    <text class="year-number" transform="translate(871,247) rotate(90)">10</text>
    <text class="year-number" transform="translate(871,367.2) rotate(90)">20</text>
    <text class="year-number" transform="translate(871,487.4) rotate(90)">30</text>
    <text class="year-number" transform="translate(871,607.6) rotate(90)">40</text>
    <text class="year-number" transform="translate(871,727.8) rotate(90)">50</text>
    <text class="year-number" transform="translate(871,848) rotate(90)">60</text>
    <text class="year-number" transform="translate(871,968.2) rotate(90)">70</text>
    <text class="year-number" transform="translate(871,1088.4) rotate(90)">80</text>
  </g>

  <!-- Weeks of life grid: 8 decades × 2 halves of the year -->
  <g class="life-grid">
    <use href="#half-decade" x="124" y="141"/>
    <use href="#half-decade" x="502" y="141"/>
    <use href="#half-decade" x="124" y="261.2"/>
    <use href="#half-decade" x="502" y="261.2"/>
    <use href="#half-decade" x="124" y="381.4"/>
    <use href="#half-decade" x="502" y="381.4"/>
    <use href="#half-decade" x="124" y="501.6"/>
    <use href="#half-decade" x="502" y="501.6"/>
    <use href="#half-decade" x="124" y="621.8"/>
    <use href="#half-decade" x="502" y="621.8"/>
    <use href="#half-decade" x="124" y="742"/>
    <use href="#half-decade" x="502" y="742"/>
    <use href="#half-decade" x="124" y="862.2"/>
    <use href="#half-decade" x="502" y="862.2"/>
    <use href="#half-decade" x="124" y="982.4"/>
    <use href="#half-decade" x="502" y="982.4"/>
  </g>

  <!-- Five-week markers between decades -->
  <g class="week-marker-rows">
    <use href="#week-markers" y="254.1"/>
    <use href="#week-markers" y="374.3"/>
    <use href="#week-markers" y="494.5"/>
    <use href="#week-markers" y="614.7"/>
    <use href="#week-markers" y="734.9"/>
    <use href="#week-markers" y="855.1"/>
    <use href="#week-markers" y="975.3"/>
  </g>

  <!-- Five-year markers at both edges -->
  <g class="year-marker-rows">
    <use href="#year-markers" y="188"/>
    <use href="#year-markers" y="308.2"/>
    <use href="#year-markers" y="428.4"/>
    <use href="#year-markers" y="548.6"/>
    <use href="#year-markers" y="668.8"/>
    <use href="#year-markers" y="789"/>
    <use href="#year-markers" y="909.2"/>
    <use href="#year-markers" y="1029.4"/>
  </g>

  <!-- Quote -->
  <text class="quote" x="470" y="1139" text-anchor="middle">“Life can only be understood backwards; but it must be lived forwards.”</text>
  <text class="quote-author" x="470" y="1159" text-anchor="middle">Anselm Brodtvik</text>
</svg>
</body>
</html>
```